Business Card For Kelmora Financial Consulting

Hi, I would like a business card designed. Bold, modern.
Please use the same design as the logo. I have also attached the website design to see the overall theme.
Wordmark Font
Color: Hex: #01AEF7

```html
<!DOCTYPE html>
<html lang="en">
<head>
<meta charset="utf-8">
<title>Kelmora Financial Consulting — Business Card</title>
<link rel="stylesheet" href="https://fonts.googleapis.com/css2?family=Montserrat:wght@400;500;600&display=swap">
<style>
  :root {
    --page-bg: #1e1f22;
    --card-navy-light: #2f4352;
    --card-navy: #1b2a37;
    --card-navy-dark: #0d1620;
    --card-black: #07090c;
    --brand-blue: #01aef7;
    --text-light: #e8eef2;
    --text-muted: #c9d3da;
  }
  * { margin: 0; padding: 0; box-sizing: border-box; }
  html, body { width: 1200px; height: 960px; overflow: hidden; }
  body {
    background: var(--page-bg);
    font-family: "Montserrat", sans-serif;
    display: flex;
    flex-direction: column;
    align-items: center;
    justify-content: center;
    gap: 48px;
  }
  .card {
    position: relative;
    width: 728px;
    height: 416px;
    border-radius: 4px;
    overflow: hidden;
    box-shadow: 0 18px 40px rgba(0,0,0,0.55);
  }

  /* Front */
  .card--front {
    background: radial-gradient(ellipse at 48% 42%, var(--card-navy-light) 0%, var(--card-navy) 45%, var(--card-navy-dark) 100%);
  }
  .person {
    position: absolute;
    left: 60px;
    top: 82px;
  }
  .person__rule {
    position: absolute;
    left: -60px;
    top: 16px;
    width: 50px;
    height: 2px;
    background: var(--brand-blue);
  }
  .person__name {
    font-size: 28px;
    font-weight: 500;
    color: var(--brand-blue);
    letter-spacing: 0.5px;
  }
  .person__title {
    margin-top: 4px;
    margin-left: 16px;
    font-size: 17px;
    font-weight: 500;
    color: var(--text-muted);
  }
  .contact-list {
    position: absolute;
    left: 36px;
    top: 182px;
    list-style: none;
  }
  .contact-list__item {
    display: flex;
    align-items: center;
    gap: 14px;
    height: 32px;
    font-size: 17px;
    color: var(--text-light);
  }
  .contact-list__icon { width: 18px; height: 18px; flex: none; }
  .contact-list__address {
    margin-top: 6px;
    font-size: 17px;
    line-height: 1.45;
    color: var(--text-light);
  }
  .wordmark {
    position: absolute;
    display: flex;
    align-items: center;
    gap: 14px;
    color: var(--text-light);
    font-weight: 600;
  }
  .wordmark__square {
    width: 34px;
    height: 34px;
    background: var(--brand-blue);
    flex: none;
  }
  .wordmark__name { font-size: 36px; letter-spacing: 3px; line-height: 1; }
  .wordmark__tag { font-size: 12px; letter-spacing: 10px; margin-top: 8px; }
  .card--front .wordmark { right: 52px; bottom: 70px; }

  /* Back */
  .card--back { background: var(--card-black); }
  .card--back .wordmark { left: 70px; top: 58px; }
  .chart-art {
    position: absolute;
    left: 120px;
    top: 170px;
    width: 560px;
    height: 220px;
    background:
      radial-gradient(ellipse at 40% 80%, rgba(1,174,247,0.55) 0%, rgba(1,174,247,0.18) 40%, rgba(7,9,12,0) 72%),
      linear-gradient(180deg, #07090c 0%, #0b2236 60%, #07090c 100%);
  }
</style>
</head>
<body>

  <section class="card card--front" aria-label="Business card front">
    <div class="person">
      <span class="person__rule"></span>
      <h1 class="person__name">IAN PORTER</h1>
      <p class="person__title">Chairman</p>
    </div>

    <ul class="contact-list">
      <li class="contact-list__item">
        <svg class="contact-list__icon" viewBox="0 0 24 24" aria-hidden="true">
          <path d="M6.6 10.8a15 15 0 0 0 6.6 6.6l2.2-2.2c.3-.3.7-.4 1-.2 1.1.4 2.3.6 3.6.6.6 0 1 .4 1 1V20c0 .6-.4 1-1 1A17 17 0 0 1 3 4c0-.6.4-1 1-1h3.5c.6 0 1 .4 1 1 0 1.3.2 2.5.6 3.6.1.3 0 .7-.2 1z" fill="#01aef7"/>
        </svg>
        +1 555 014 2290
      </li>
      <li class="contact-list__item">
        <svg class="contact-list__icon" viewBox="0 0 24 24" aria-hidden="true">
          <rect x="2" y="5" width="20" height="14" rx="1" fill="#01aef7"/>
          <path d="M2.5 5.8 12 13l9.5-7.2" fill="none" stroke="#1b2a37" stroke-width="1.6"/>
        </svg>
        hello@kelmorafinancial.com
      </li>
      <li class="contact-list__item">
        <svg class="contact-list__icon" viewBox="0 0 24 24" aria-hidden="true">
          <circle cx="12" cy="12" r="9.5" fill="none" stroke="#01aef7" stroke-width="2"/>
          <ellipse cx="12" cy="12" rx="4" ry="9.5" fill="none" stroke="#01aef7" stroke-width="1.6"/>
          <path d="M2.5 12h19M4 7h16M4 17h16" stroke="#01aef7" stroke-width="1.4"/>
        </svg>
        www.kelmorafinancial.com
      </li>
    </ul>
    <p class="contact-list__address" style="position:absolute;left:36px;top:288px;">
      2218 Linden Row Suite 12,<br>Fairhaven
    </p>

    <div class="wordmark">
      <span class="wordmark__square"></span>
      <div>
        <div class="wordmark__name">KELMORA</div>
        <div class="wordmark__tag">CONSULTING</div>
      </div>
    </div>
  </section>

  <section class="card card--back" aria-label="Business card back">
    <div class="wordmark">
      <span class="wordmark__square"></span>
      <div>
        <div class="wordmark__name">KELMORA</div>
        <div class="wordmark__tag">CONSULTING</div>
      </div>
    </div>
    <div class="chart-art" role="img" aria-label="Glowing blue 3D bar chart rising across a dark reflective surface"></div>
  </section>

</body>
</html>
```